Law Firm Website

We are looking to update our old, tired and very flat website. We have someone who will code and host the site but we need some design inspiration. The website will consist of no more than 2/3 pages, possibly with pop-ups for information. We already have all the blurb. We would like something distinctive, clean and eye-catching, using the purple and white theme that we already use on our firm stationery. Examples uploaded. Current website URL is www.dunmorewillett.example.

Industry/Entity Type

Law Firm

```html
<!DOCTYPE html>
<html lang="en">
<head>
<meta charset="utf-8">
<title>Dunmore + Willett Solicitors</title>
<link rel="stylesheet" href="https://fonts.googleapis.com/css2?family=Open+Sans:wght@400;600;700&family=Nunito:wght@300;400;600&display=swap">
<style>
:root{
  --purple:#5a4e9c;
  --purple-dark:#4a3f8a;
  --purple-band-a:#6a5fb0;
  --purple-band-b:#4f4596;
  --ink:#24332c;
  --text:#444;
  --muted:#777;
  --white:#fff;
  --line:#cfcfcf;
  --dark:#2a2a2a;
  --footer:#e6e6e6;
  --link-blue:#2a7fc0;
}
*{box-sizing:border-box;margin:0;padding:0}
html,body{width:819px;height:1200px;overflow:hidden}
body{position:relative;background:var(--white);font-family:"Open Sans",Arial,sans-serif;color:var(--text)}
.abs{position:absolute}
.top-band{left:0;top:0;width:819px;height:337px;background:linear-gradient(120deg,var(--purple-band-a),var(--purple-band-b) 45%,var(--purple-band-a) 70%,var(--purple-band-b))}
.top-fade{left:0;top:337px;width:819px;height:30px;background:linear-gradient(#eee,#fff)}
.page{left:99px;top:13px;width:620px;height:600px;background:var(--white)}
.logo{left:115px;top:38px}
.logo-name{font-weight:700;font-size:35px;color:var(--ink);letter-spacing:-.5px;line-height:1}
.logo-sub{font-weight:700;font-size:16px;color:var(--purple);margin-left:56px;margin-top:2px}
.search{left:556px;top:41px;width:144px;height:19px;border:1px solid var(--line);font-size:9px;color:var(--muted);padding:3px 8px}
.search svg{position:absolute;right:5px;top:3px}
.nav{right:119px;top:82px;display:flex;gap:18px;font-size:9px;font-weight:600;color:#555}
.hero{left:115px;top:117px;width:585px;height:220px;background:radial-gradient(ellipse at 62% 45%,#6b6b6b,#3a3a3a 55%,#1d1d1d)}
.hero-kicker{left:143px;top:177px;width:240px;text-align:center;color:var(--white);font-family:"Nunito",sans-serif;font-size:16px}
.hero-kicker::before,.hero-kicker::after{content:"";position:absolute;top:11px;width:48px;height:1px;background:#aaa}
.hero-kicker::before{left:0}.hero-kicker::after{right:0}
.hero-title{left:143px;top:207px;width:240px;text-align:center;color:var(--white);font-family:"Nunito",sans-serif;font-size:28px;font-weight:600;line-height:39px}
.dots{left:390px;top:318px;display:flex;gap:3px}
.dots span{width:9px;height:9px;border-radius:50%;background:#ddd}
.quote{left:502px;top:287px;width:191px;height:300px;background:var(--white);border-radius:5px 5px 0 0;box-shadow:0 0 12px rgba(0,0,0,.12)}
.quote h3{text-align:center;font-weight:400;font-size:13px;color:var(--purple);margin-top:20px;letter-spacing:-.2px}
.field{position:absolute;left:10px;width:174px;height:24px;border:1px solid var(--line);font-size:8px;color:#666;padding:5px 8px}
.btn{position:absolute;left:31px;top:227px;width:136px;height:27px;background:var(--purple);color:var(--white);font-size:11px;text-align:center;line-height:27px;border-radius:2px;box-shadow:0 2px 0 var(--purple-dark)}
.welcome{left:115px;top:361px;width:365px}
.welcome h1{font-family:"Nunito",sans-serif;font-weight:400;font-size:20px;color:var(--purple);margin-bottom:8px}
.lead{font-size:8.6px;color:#333;line-height:14px;margin-bottom:5px}
.body-copy{font-size:7.6px;color:#555;line-height:13px}
.welcome h2{font-family:"Nunito",sans-serif;font-weight:400;font-size:12.5px;color:var(--purple);margin-top:12px;margin-bottom:6px}
.expertise{display:grid;grid-template-columns:128px 128px 120px;row-gap:7px;font-size:8.8px;color:#444}
.expertise li{list-style:none;display:flex;align-items:center;gap:10px;height:14px}
.team{left:0;top:597px;width:819px;height:305px;background:linear-gradient(#3a3a3a,#232323 60%,#2e2e2e)}
.team h2{position:absolute;top:40px;width:819px;text-align:center;font-family:"Nunito",sans-serif;font-weight:400;font-size:20px;color:var(--white)}
.portrait{position:absolute;top:90px;width:134px;height:155px;border-radius:4px;background:linear-gradient(#7c8190,#44495a)}
.portrait.mono{background:linear-gradient(#9a9a9a,#2a2a2a)}
.amp{position:absolute;left:392px;top:128px;font-size:56px;color:#777;font-family:"Nunito",sans-serif;font-weight:300}
.partner-name{position:absolute;top:258px;width:134px;text-align:center;color:var(--white);font-size:14px;font-family:"Nunito",sans-serif;font-weight:600}
.reviews-title{left:0;top:937px;width:819px;text-align:center;font-family:"Nunito",sans-serif;font-size:20px;color:var(--purple)}
.avatar{top:988px;width:82px;height:82px;border-radius:50%;border:2px solid #ddd;background:linear-gradient(#c9d3dc,#5b6470)}
.review{top:998px;width:172px;font-size:7.6px;color:#888;line-height:15px}
.review .mark{position:absolute;font-size:22px;color:#bbb;font-family:Georgia,serif;line-height:1}
.review p{padding-left:14px}
.review .by{display:block;text-align:right;color:var(--link-blue);font-size:7.6px;margin-top:7px}
.footer{left:0;top:1114px;width:819px;height:86px;background:var(--footer)}
.footer-links{left:114px;top:1141px;font-size:8px;color:#333}
.copyright{left:114px;top:1161px;font-size:8px;color:#333}
.badge{left:419px;top:1141px;width:116px;height:34px;background:var(--white);border:1px solid #d5d5d5}
.social{left:593px;top:1147px;display:flex;gap:9px}
.social span{width:21px;height:21px}
</style>
</head>
<body>
<div class="abs top-band"></div>
<div class="abs top-fade"></div>
<div class="abs page"></div>

<header>
  <div class="abs logo">
    <div class="logo-name">Dunmore + Willett</div>
    <div class="logo-sub">Solicitors</div>
  </div>
  <div class="abs search">Search
    <svg width="11" height="11" viewBox="0 0 11 11"><circle cx="4.5" cy="4.5" r="3.2" fill="none" stroke="#222" stroke-width="1.6"/><line x1="7" y1="7" x2="10" y2="10" stroke="#222" stroke-width="2"/></svg>
  </div>
  <nav class="abs nav"><span>HOME</span><span>AREAS OF EXPERTISE</span><span>DANIEL DUNMORE</span><span>PETER WILLETT</span><span>CONTACT</span></nav>
</header>

<section>
  <div class="abs hero" role="img" aria-label="Monochrome photo of a statue of Justice holding balance scales"></div>
  <div class="abs hero-kicker">COMPRHENSIVE</div>
  <div class="abs hero-title">LEGAL<br>INFORMATION</div>
  <div class="abs dots"><span></span><span></span><span></span><span></span></div>
</section>

<aside class="abs quote">
  <h3>REQUEST A FREE QUOTE!</h3>
  <div class="field" style="top:51px">Name</div>
  <div class="field" style="top:86px">Phone</div>
  <div class="field" style="top:121px">E-mail</div>
  <div class="field" style="top:156px;height:66px">Message</div>
  <div class="btn">Submit Request</div>
</aside>

<section class="abs welcome">
  <h1>Welcome To Our Website</h1>
  <p class="lead">Morbi accumsan ipsum velit. Nam nec tellus a odio tincidunt auctor a ornare odio. Sed non&nbsp; mauris vitae erat Lorem Ipsum is simply dummy text of the printing.</p>
  <p class="body-copy">Lorem ipsum dolor sit amet, consectetuer adipiscing elit. Sed elit. Nulla sem risus, vestibulum in, vol utpat eget, dapibus ac, lectus. Curabitur dolor sapien, hendrerit non, suscipit bibendum, auctor ac.</p>
  <h2>Main Areas Of Expertise</h2>
  <ul class="expertise">
    <li><svg width="12" height="10" viewBox="0 0 12 10"><path d="M1 5l3.5 3.5L11 1.5" fill="none" stroke="var(--purple)" stroke-width="2.2"/></svg>Litigation</li>
    <li><svg width="12" height="10" viewBox="0 0 12 10"><path d="M1 5l3.5 3.5L11 1.5" fill="none" stroke="var(--purple)" stroke-width="2.2"/></svg>Wills &amp; Probate</li>
    <li><svg width="12" height="10" viewBox="0 0 12 10"><path d="M1 5l3.5 3.5L11 1.5" fill="none" stroke="var(--purple)" stroke-width="2.2"/></svg>Intellectual Property</li>
    <li><svg width="12" height="10" viewBox="0 0 12 10"><path d="M1 5l3.5 3.5L11 1.5" fill="none" stroke="var(--purple)" stroke-width="2.2"/></svg>Company Matters</li>
    <li><svg width="12" height="10" viewBox="0 0 12 10"><path d="M1 5l3.5 3.5L11 1.5" fill="none" stroke="var(--purple)" stroke-width="2.2"/></svg>Landlord &amp; Tenant</li>
    <li><svg width="12" height="10" viewBox="0 0 12 10"><path d="M1 5l3.5 3.5L11 1.5" fill="none" stroke="var(--purple)" stroke-width="2.2"/></svg>Commercial Crime</li>
    <li><svg width="12" height="10" viewBox="0 0 12 10"><path d="M1 5l3.5 3.5L11 1.5" fill="none" stroke="var(--purple)" stroke-width="2.2"/></svg>Insolvency</li>
    <li><svg width="12" height="10" viewBox="0 0 12 10"><path d="M1 5l3.5 3.5L11 1.5" fill="none" stroke="var(--purple)" stroke-width="2.2"/></svg>Divorce</li>
    <li><svg width="12" height="10" viewBox="0 0 12 10"><path d="M1 5l3.5 3.5L11 1.5" fill="none" stroke="var(--purple)" stroke-width="2.2"/></svg>Media Law</li>
    <li><svg width="12" height="10" viewBox="0 0 12 10"><path d="M1 5l3.5 3.5L11 1.5" fill="none" stroke="var(--purple)" stroke-width="2.2"/></svg>Conveyancing</li>
    <li><svg width="12" height="10" viewBox="0 0 12 10"><path d="M1 5l3.5 3.5L11 1.5" fill="none" stroke="var(--purple)" stroke-width="2.2"/></svg>Care of the Elderly</li>
    <li><svg width="12" height="10" viewBox="0 0 12 10"><path d="M1 5l3.5 3.5L11 1.5" fill="none" stroke="var(--purple)" stroke-width="2.2"/></svg>Commercial</li>
  </ul>
</section>

<section class="abs team" role="img" aria-label="Dark city skyline photo behind the partners">
  <h2>Dunmore &amp; Willett Solicitors, For the service you deserve</h2>
  <div class="portrait" style="left:227px" role="img" aria-label="Portrait photo of partner Daniel Dunmore"></div>
  <div class="amp">&amp;</div>
  <div class="portrait mono" style="left:458px" role="img" aria-label="Black and white portrait photo of partner Peter Willett"></div>
  <div class="partner-name" style="left:227px">Daniel Dunmore</div>
  <div class="partner-name" style="left:458px">Peter Willett</div>
</section>

<section>
  <h2 class="abs reviews-title">What Our Clients Are Saying?</h2>
  <div class="abs avatar" style="left:117px" role="img" aria-label="Client photo of Owen Hartley"></div>
  <div class="abs review" style="left:210px">
    <span class="mark">&ldquo;</span>
    <p>Claritas est etiam processus dynamic sequitur mutationem consuetudium lectorum. Mirenot are quam littera gothica, quam nunc.</p>
    <span class="by">- Owen Hartley</span>
  </div>
  <div class="abs avatar" style="left:431px" role="img" aria-label="Client photo of Laura Benning"></div>
  <div class="abs review" style="left:524px">
    <span class="mark">&ldquo;</span>
    <p>Claritas est etiam processus dynamic sequitur mutationem consuetudium lectorum. Mirenot are quam littera gothica, quam nunc.</p>
    <span class="by">- Laura Benning</span>
  </div>
</section>

<footer>
  <div class="abs footer"></div>
  <div class="abs footer-links">Terms and Conditions | Privacy Promise | FAQ's | Contact Us</div>
  <div class="abs copyright">Copyright © 2013. All Rights Reserved.</div>
  <div class="abs badge" role="img" aria-label="Professional membership badge"></div>
  <div class="abs social">
    <span style="background:#3b5a9a"></span>
    <span style="background:#2aa3d8"></span>
    <span style="background:#f2781f"></span>
    <span style="background:#d92b2b"></span>
  </div>
</footer>
</body>
</html>
```